Business card design for a teacher - double sided, sleek design.

My name is Dalia and I am an online Arabic language teacher. I am looking for a beautiful business card design for my online teaching business.

The cards will be printed in 85mm x 55mm size.
The card can be either portrait or landscape.

The design should contain my logo on one side and information on the other.

The design needs to be clean and modern. Use of subtle Arabic geometric patterns would be nice. Icons for the social media information on the card should also match the design theme.

My logo font is Consolas, which is a Monospace font.

Business card design should be delivered with editable PSD or EPS files in the handover.

Thanks

Dalia

----

Information on the back:

URL: www.lughapathway.net [this should stand out more than other details]
Email: info@lughapathway.net
Instagram: @lughapathway
Facebook: circleboard.net/lughapathway
Skype: lughapathway

My brand colours are shown in the logo attached. These are:
- Teal green - 4DC9C1
- Mango yellow - FFD600

Target Market(s)

- Young professionals
- Expatriates
- Women and Men

Industry/Entity Type

Education

Contact Information for Business Card

Information on the back:

Skype: lughapathway

- Teal green - 4DC9C1
- Mango yellow - FFD600

Font styles to use
Other font styles liked:
• Any font complimentary to my logo font which is a Monospace font called Consolas.

Colors

Designer to choose colors to be used in the design.

Requirements
Must have
• - Aesthetically pleasing look
• - Complimentary design with existing logo
Nice to have
• Arabic geometrical patterns

```html
<!DOCTYPE html>
<html lang="en">
<head>
<meta charset="utf-8">
<title>Lugha Pathway — Business Card</title>
<link rel="stylesheet" href="https://fonts.googleapis.com/css2?family=Inconsolata:wght@400;700&family=Source+Sans+3:wght@400;600&display=swap">
<style>
  :root {
    --bg: #e7e4df;
    --card: #2d2d2f;
    --card-edge: #242426;
    --teal: #4dc9c1;
    --mango: #ffd600;
    --ink: #f2f2f2;
    --social: #3b5a9a;
    --envelope: #f6d64a;
    --envelope-line: #8a6f10;
    --mono: "Inconsolata", monospace;
    --sans: "Source Sans 3", sans-serif;
  }
  * { margin: 0; padding: 0; box-sizing: border-box; }
  html, body { width: 1200px; height: 900px; overflow: hidden; }
  body { background: var(--bg); position: relative; font-family: var(--mono); }

  .card {
    position: absolute;
    width: 580px;
    height: 375px;
    background: radial-gradient(ellipse at 50% 40%, #333335 0%, var(--card) 60%, var(--card-edge) 100%);
    border-radius: 4px;
    box-shadow: 0 14px 30px rgba(0,0,0,.25);
    overflow: hidden;
  }
  .card--front { left: 110px; top: 60px; }
  .card--back  { left: 510px; top: 465px; }

  /* Front */
  .brand {
    position: absolute;
    left: 50%; top: 50%;
    transform: translate(-50%, -50%);
    display: flex; align-items: center; gap: 22px;
  }
  .brand__square {
    width: 92px; height: 92px;
    border: 4px solid var(--mango);
    flex: none;
  }
  .brand__name {
    font-family: var(--mono);
    font-weight: 700;
    font-size: 36px;
    letter-spacing: 4px;
    color: var(--teal);
    text-transform: uppercase;
    line-height: 1.1;
    white-space: nowrap;
  }

  /* Back */
  .back-logo {
    position: absolute;
    left: 40px; top: 118px;
    width: 172px;
    display: flex; flex-direction: column; align-items: center; gap: 12px;
  }
  .back-logo .brand__square { width: 118px; height: 118px; }
  .back-logo .brand__name { font-size: 17px; letter-spacing: 3px; line-height: 1; }

  .divider {
    position: absolute;
    left: 232px; top: 100px;
    width: 1px; height: 170px;
    background: linear-gradient(var(--teal), var(--mango));
  }

  .person {
    position: absolute;
    left: 300px; top: 38px; width: 250px;
    text-align: center;
  }
  .person__name {
    font-family: var(--sans);
    font-weight: 600;
    font-size: 32px;
    letter-spacing: 3px;
    text-transform: uppercase;
    background: linear-gradient(90deg, var(--mango) 20%, var(--teal) 80%);
    -webkit-background-clip: text;
    background-clip: text;
    color: transparent;
    line-height: 1;
    display: inline-block;
  }
  .person__role {
    font-family: var(--sans);
    font-size: 15px;
    color: var(--ink);
    line-height: 1.2;
  }
  .person__rule {
    height: 1px; margin-top: 4px;
    background: var(--mango);
    opacity: .7;
  }

  .contacts__rule {
    position: absolute; left: 258px; top: 118px;
    width: 292px; height: 1px; background: var(--teal); opacity: .7;
  }
  .contacts {
    position: absolute;
    left: 258px; top: 128px;
    list-style: none;
  }
  .contact {
    display: flex; align-items: center; gap: 12px;
    height: 30px;
    font-size: 14px;
    letter-spacing: 1px;
    color: var(--ink);
    white-space: nowrap;
  }
  .contact__mark { width: 20px; height: 20px; flex: none; }
  .contact__mark--chat { background: var(--teal); border-radius: 50%; }
  .contact__mark--photo { background: var(--mango); border-radius: 4px; }
  .contact__mark--social { background: var(--social); border-radius: 3px; }
  .contact__icon { width: 20px; height: 15px; flex: none; }

  .website {
    position: absolute;
    left: 258px; bottom: 40px;
    font-size: 20px;
    letter-spacing: 2px;
    color: var(--ink);
    white-space: nowrap;
  }
</style>
</head>
<body>

  <section class="card card--front" aria-label="Card front">
    <div class="brand">
      <div class="brand__square"></div>
      <div class="brand__name">Lugha<br>Pathway</div>
    </div>
  </section>

  <section class="card card--back" aria-label="Card back">
    <div class="back-logo">
      <div class="brand__square"></div>
      <div class="brand__name">Lugha Pathway</div>
    </div>

    <div class="divider"></div>

    <header class="person">
      <h1 class="person__name">Dalia</h1>
      <p class="person__role">Teacher</p>
      <div class="person__rule"></div>
    </header>

    <div class="contacts__rule"></div>
    <ul class="contacts">
      <li class="contact"><span class="contact__mark contact__mark--chat"></span>lughapathway</li>
      <li class="contact"><span class="contact__mark contact__mark--photo"></span>@lughapathway</li>
      <li class="contact"><span class="contact__mark contact__mark--social"></span>circleboard.net/lughapathway</li>
      <li class="contact">
        <svg class="contact__icon" viewBox="0 0 22 16" aria-hidden="true">
          <rect x="0.5" y="0.5" width="21" height="15" fill="var(--envelope)"/>
          <path d="M1 1 L11 9 L21 1" fill="none" stroke="var(--envelope-line)" stroke-width="1.2"/>
        </svg>
        info@lughapathway.net
      </li>
    </ul>

    <p class="website">www.lughapathway.net</p>
  </section>

</body>
</html>
```